Letterhead needed using basic elements of our new logo!

We have just had a new logo and business card created on Pixel Harbor and now would like a new letterhead for our company re-branding. Our logo inspires trust, professionalism and confidence and we would like to mirror that in our letterhead. We would like to use elements in our logo (as well as the logo itself, obviously), but understand with only a header and the ability to print in black and white, we are somewhat limited. We have also won the Resident's Pick Medal for best Property Management Company in our city and would like to somehow include that small banner (see uploaded file) in the letterhead, without it clashing?

Text to include:
Stonebrook Property Management (and logo)
C-214 Marlowe Ave, Winnipeg, MB R2K 3P7
Ph: 204-738-2915
Fax: 1-888-276-9413
Email: customerservice@stonebrookpropertymanagement.example
Web: www.stonebrookpropertymanagement.example

Pasted below is our mission, vision and branding statements to help with the project:

Mission Statement

Provide the highest quality customer service to both property owners and tenants using innovative technology and well trained, caring staff.

Vision Statement

To redefine the way in which management is delivered to its customers, becoming the recognized leader in the property management industry.

Brand Essence

When our customers experience our product or service, it brings forth an emotion of absolute trust that we have their best interests at heart

Brand Personality

We are a company that is passionate about our customers, our company and our vision to be leaders in the field of property management. We are visionaries that aren't afraid to use cutting edge technologies to improve our products and service.

Position or Value Proposition

To whom are we speaking?
- real estate investors, including first timers that are giving us their first starter home. They are fairly naive, as they are not "big time" investors, and because they are giving us their first home (in contract to an investor buying a rental property, often sight unseen) they are more emotionally tied to their property and will require a company that inspires trust and confidence.

What is our brand promise?
- we will do our best to serve our clients, both owners and tenants, to give them prompt communication, clear, concise answers to their questions, and look after their property quickly and competently.

Why is our product different than the competition and why should our customers care?
- the current model used by most management companies employs individual portfolio managers that do things a little differently each instance, and differently than their fellow staff members. Our management product is superior because we use a combination of technology and strict procedures to ensure each client's experience is consistent, each and every time.

Industry/Entity Type

Business

Requirements
Must have
• We would like an option to be in black and white, to be able to be printed from Microsoft Word. As well, we do not want anything in a footer or any other kind of letterhead that bleeds below a header. The main use of this letterhead will be from our property management software, to be used in our form letters and other templates (sent to tenants and clients)
Should not have
• Footer or other elements where the text body would be, it will be used in a form letter

```html
<!DOCTYPE html>
<html lang="en">
<head>
<meta charset="utf-8">
<title>Stonebrook Property Management – Letterhead</title>
<link rel="stylesheet" href="https://fonts.googleapis.com/css2?family=Lato:wght@400;700&display=swap">
<style>
  :root {
    --backdrop: #e4e4e4;
    --paper: #ffffff;
    --brand-blue: #1e8fd6;
    --brand-dark: #333a40;
    --text: #3a3a3a;
    --medal-fill: #eef1f4;
    --medal-edge: #c9d0d6;
  }
  * { margin: 0; padding: 0; box-sizing: border-box; }
  html, body {
    width: 1200px;
    height: 1200px;
    overflow: hidden;
    background: var(--backdrop);
    font-family: "Lato", Arial, sans-serif;
  }
  .letterhead {
    position: absolute;
    left: 258px;
    top: 124px;
    width: 652px;
    height: 924px;
    background: var(--paper);
    overflow: hidden;
    box-shadow: 0 2px 10px rgba(0,0,0,0.15);
  }
  .brand {
    position: absolute;
    left: 54px;
    top: 58px;
    display: flex;
    align-items: center;
    gap: 9px;
  }
  .brand-square {
    width: 36px;
    height: 36px;
    background: var(--brand-dark);
  }
  .brand-name {
    font-weight: 700;
    font-size: 15px;
    line-height: 1.15;
    color: var(--brand-blue);
    width: 150px;
    letter-spacing: 0.3px;
  }
  .medal {
    position: absolute;
    left: 262px;
    top: 52px;
    width: 48px;
    height: 48px;
    border-radius: 50%;
    background: var(--medal-fill);
    border: 2px solid var(--medal-edge);
  }
  .contact {
    position: absolute;
    left: 340px;
    top: 53px;
    width: 256px;
    font-size: 9.5px;
    font-style: normal;
    color: var(--text);
  }
  .contact-address {
    padding-bottom: 5px;
    border-bottom: 1px solid var(--brand-blue);
    margin-bottom: 6px;
  }
  .contact-line {
    display: flex;
    align-items: center;
    height: 14px;
    white-space: nowrap;
  }
  .contact-line svg {
    width: 9px;
    height: 9px;
    margin-right: 3px;
    flex: none;
  }
  .divider { color: var(--brand-blue); margin: 0 4px; }
</style>
</head>
<body>
  <main class="letterhead">
    <header>
      <div class="brand">
        <span class="brand-square"></span>
        <span class="brand-name">Stonebrook Property Management</span>
      </div>
      <div class="medal" role="img" aria-label="Resident's Pick Medal badge"></div>
      <address class="contact">
        <div class="contact-address">C-214 Marlowe Ave, Winnipeg, MB R2K 3P7</div>
        <div class="contact-line">
          <svg viewBox="0 0 10 10"><path d="M2 1 L4 1 L4.6 3 L3.5 4 Q4.5 6 6 6.6 L7 5.5 L9 6 L9 8 Q8 9.3 6 8.6 Q2.2 7 1.2 3 Q1 1.5 2 1Z" fill="#1e8fd6"/></svg>
          204-738-2915
          <span class="divider">|</span>
          <svg viewBox="0 0 10 10"><rect x="3" y="1" width="4" height="2.5" fill="#1e8fd6"/><rect x="1" y="3.5" width="8" height="3.5" rx="0.8" fill="#1e8fd6"/><rect x="3" y="6" width="4" height="3" fill="#fff" stroke="#1e8fd6" stroke-width="0.8"/></svg>
          1-888-276-9413
        </div>
        <div class="contact-line">
          <svg viewBox="0 0 10 10"><rect x="1" y="2.5" width="8" height="5.5" fill="#1e8fd6"/><path d="M1 2.5 L5 5.5 L9 2.5" fill="none" stroke="#fff" stroke-width="0.8"/></svg>
          customerservice@stonebrookpropertymanagement.example
        </div>
        <div class="contact-line">
          <svg viewBox="0 0 10 10"><circle cx="5" cy="5" r="4" fill="none" stroke="#1e8fd6" stroke-width="0.9"/><ellipse cx="5" cy="5" rx="1.8" ry="4" fill="none" stroke="#1e8fd6" stroke-width="0.7"/><line x1="1" y1="5" x2="9" y2="5" stroke="#1e8fd6" stroke-width="0.7"/></svg>
          www.stonebrookpropertymanagement.example
        </div>
      </address>
    </header>
  </main>
</body>
</html>
```